Creative, fresh business card design for Orrin Linings

We need a fresh, creative business card design for Orrin Linings. We are the manufacturer of Orrin Linings in Australia. Wall panels are 2400 x 1200mm panels made from MDF and feature 3D patterns on the face of the panel. The colours to be used are green, silver/grey and white RGB
Red 187
Green 207
Blue 65.

An idea is to possibly use a watermark of one of our designs as a background (like on the "Ferns" design on the left hand side of page 2 of our brochure).

Target Market(s)

Interior designers, architects, builders and home renovators

Industry/Entity Type

Business

Contact Information for Business Card

Details to go on the card are:
Our logo (attached),
Slogan: "Decorative panels for interiors and exteriors",
Contact name,
Position,
Mobile phone number,
Business address,
Business phone,
Business fax,
Website and
Email address.

I have attached a few images of our panels and our brochure for reference.

The colours of the business card should feature our logo colours which are: RGB
Red 187
Green 207
Blue 65

Requirements
Must have
• Very modern fonts and design. Some of the designs shown especially the "Weave" design which is a popular design.
Nice to have
• Creative but simple design. Very contemporary.
Should not have
• Anything ornate or old fashioned.

```html
<!DOCTYPE html>
<html lang="en">
<head>
<meta charset="utf-8">
<title>Orrin Linings – Business Card</title>
<link rel="stylesheet" href="https://fonts.googleapis.com/css2?family=Open+Sans:wght@400;600;700&display=swap">
<style>
  :root {
    --brand-green: rgb(187, 207, 65);
    --brand-grey: #8e8f93;
    --pattern-light: #f4f4f5;
    --pattern-mid: #dcdcde;
    --card-white: #ffffff;
    --card-black: #262626;
    --ink: #1d1d1f;
    --ink-soft: #4a4a4d;
    --backdrop: #ecebe8;
  }
  * { box-sizing: border-box; margin: 0; padding: 0; }
  html, body {
    width: 1200px; height: 900px; overflow: hidden;
    background: var(--backdrop);
    font-family: "Open Sans", Arial, sans-serif;
  }
  .stage { position: relative; width: 1200px; height: 900px; }

  .card {
    position: absolute;
    width: 620px; height: 354px;
    overflow: hidden;
    box-shadow: 0 10px 24px rgba(0,0,0,.18);
  }

  /* Back side */
  .card--back { left: 500px; top: 80px; background: var(--card-black); }
  .card--back .brand {
    position: absolute; left: 0; right: 0; top: 120px;
    display: flex; flex-direction: column; align-items: center;
  }
  .brand__row { display: flex; align-items: center; gap: 14px; }
  .brand__square { width: 34px; height: 34px; }
  .brand__name { font-weight: 700; font-size: 40px; letter-spacing: .5px; line-height: 1; }
  .brand__slogan {
    margin-top: 16px; font-size: 14px; letter-spacing: 4px;
    text-transform: lowercase; line-height: 1.35; text-align: center;
  }
  .card--back .brand__square { background: var(--card-white); }
  .card--back .brand__name { color: var(--card-white); }
  .card--back .brand__slogan { color: #cfcfcf; }

  /* Front side */
  .card--front { left: 80px; top: 470px; background: var(--card-white); }
  .front__pattern {
    position: absolute; right: 0; top: 0; width: 230px; height: 354px;
    background: linear-gradient(135deg, var(--pattern-light) 0%, var(--pattern-mid) 55%, var(--pattern-light) 100%);
  }
  .front__bands { position: absolute; inset: 0; }

  .contact { position: absolute; left: 0; top: 0; }
  .contact__name {
    position: absolute; left: 62px; top: 26px;
    font-weight: 700; font-size: 21px; color: var(--ink); white-space: nowrap;
  }
  .contact__role {
    position: absolute; left: 62px; top: 55px;
    font-size: 13px; color: var(--ink-soft); white-space: nowrap;
  }
  .contact__address {
    position: absolute; left: 50px; top: 96px;
    font-size: 14px; line-height: 1.35; color: var(--ink); white-space: nowrap;
  }
  .contact__list {
    position: absolute; left: 30px; top: 148px; list-style: none;
  }
  .contact__item {
    display: flex; align-items: center; gap: 10px;
    height: 22px; font-size: 14px; color: var(--ink); white-space: nowrap;
  }
  .contact__icon { width: 12px; height: 12px; flex: none; }

  .card--front .brand {
    position: absolute; left: 300px; top: 138px;
    display: flex; flex-direction: column; align-items: flex-start;
  }
  .card--front .brand__square { background: var(--brand-green); }
  .card--front .brand__name { color: var(--brand-grey); font-size: 36px; }
  .card--front .brand__slogan { color: var(--brand-grey); text-align: left; font-size: 13px; }
</style>
</head>
<body>
<main class="stage">

  <section class="card card--back" aria-label="Business card, back">
    <div class="brand">
      <div class="brand__row">
        <span class="brand__square"></span>
        <span class="brand__name">Orrin Linings</span>
      </div>
      <p class="brand__slogan">decorative panels for<br>interiors &amp; landscapes</p>
    </div>
  </section>

  <section class="card card--front" aria-label="Business card, front">
    <div class="front__pattern" role="img" aria-label="Faint white 3D faceted wall panel pattern"></div>

    <svg class="front__bands" width="620" height="354" viewBox="0 0 620 354" aria-hidden="true">
      <polygon points="0,0 40,0 18,38 0,38" fill="var(--brand-green)"/>
      <polygon points="30,0 50,0 28,38 8,38" fill="var(--brand-grey)"/>
      <polygon points="0,270 300,270 282,298 0,298" fill="var(--brand-green)"/>
      <polygon points="290,302 620,302 620,330 272,330" fill="var(--brand-grey)"/>
    </svg>

    <div class="contact">
      <h1 class="contact__name">Marcus Hale</h1>
      <p class="contact__role">Managing Director</p>
      <p class="contact__address">12345, Address Goes Here<br>Country Name, 123456</p>
      <ul class="contact__list">
        <li class="contact__item">
          <svg class="contact__icon" viewBox="0 0 12 12"><rect x="2.5" y="0.5" width="7" height="11" rx="1.5" fill="none" stroke="var(--brand-green)" stroke-width="1.5"/></svg>
          123-456-7890
        </li>
        <li class="contact__item">
          <svg class="contact__icon" viewBox="0 0 12 12"><path d="M2 1 L4.5 1 L5.5 3.5 L4 4.8 Q5.2 7 7.2 8 L8.5 6.5 L11 7.5 L11 10 Q6 11.5 2.5 7 Q0.5 4 2 1 Z" fill="var(--brand-green)"/></svg>
          (044)-456-7890
        </li>
        <li class="contact__item">
          <svg class="contact__icon" viewBox="0 0 12 12"><rect x="1" y="4" width="10" height="7" rx="1" fill="var(--brand-green)"/><rect x="3" y="1" width="6" height="4" fill="var(--brand-green)"/></svg>
          123-456-7890
        </li>
        <li class="contact__item">
          <svg class="contact__icon" viewBox="0 0 12 12"><rect x="0.5" y="2" width="11" height="8" rx="1" fill="var(--brand-green)"/><path d="M1 2.5 L6 6.5 L11 2.5" fill="none" stroke="#fff" stroke-width="1"/></svg>
          info@youremail.com
        </li>
        <li class="contact__item">
          <svg class="contact__icon" viewBox="0 0 12 12"><circle cx="6" cy="6" r="5.5" fill="var(--brand-green)"/></svg>
          www.website.com
        </li>
      </ul>
    </div>

    <div class="brand">
      <div class="brand__row">
        <span class="brand__square"></span>
        <span class="brand__name">Orrin Linings</span>
      </div>
      <p class="brand__slogan">decorative panels for<br>interiors &amp; landscapes</p>
    </div>
  </section>

</main>
</body>
</html>
```